I need a flyer designed for a marine service company. Our company specializes in boat engine diagnostic/repair, engine service, electronic installation and repairs, bottom paint, detailing, winterization and shrink wrapping. We would like to see designs that incorporate our color scheme of deep blue, blueish gray and black (please see attached photo)

Target Market(s)

Boat owners

Industry/Entity Type

Marine

Logo Text

Kelpwick Harbor Marine Services

Requirements
Must have
• Company logo
Nice to have
• List the services we provide.

```html
<!DOCTYPE html>
<html lang="en">
<head>
<meta charset="utf-8">
<title>Kelpwick Harbor Marine Services – Flyer</title>
<link rel="stylesheet" href="https://fonts.googleapis.com/css2?family=Lexend:wght@300;400;600&display=swap">
<style>
  :root {
    --navy: #0b1a3d;
    --navy-deep: #070a26;
    --ink: #172a55;
    --orange: #e85a17;
    --amber: #f8c447;
    --mist: #e9eded;
    --white: #ffffff;
  }
  * { margin: 0; padding: 0; box-sizing: border-box; }
  html, body { width: 849px; height: 1200px; overflow: hidden; background: var(--white); }
  .flyer {
    position: relative; width: 849px; height: 1200px; overflow: hidden;
    font-family: "Lexend", sans-serif; color: var(--ink); background: var(--white);
  }
  .backdrop { position: absolute; inset: 0; }
  .hero-brand {
    position: absolute; left: 200px; top: 330px; width: 600px; text-align: center;
    color: var(--white); font-weight: 300;
  }
  .hero-brand .brand-name { font-size: 46px; letter-spacing: 1px; line-height: 1; }
  .hero-brand .brand-tag { font-size: 22px; letter-spacing: 4px; margin-top: 22px; }
  .intro { position: absolute; left: 58px; top: 748px; line-height: 1.05; color: var(--navy); }
  .intro .lead { font-size: 34px; font-weight: 400; color: var(--ink); }
  .intro .strong { font-size: 34px; font-weight: 600; }
  .services { position: absolute; left: 58px; top: 860px; list-style: none; }
  .services li {
    display: flex; align-items: center; height: 34.6px;
    font-size: 22.5px; letter-spacing: 0.4px; color: var(--navy);
  }
  .services .bullet {
    width: 20px; height: 20px; border: 2px solid var(--orange); border-radius: 50%;
    margin-right: 17px; flex: none;
  }
  .side-brand {
    position: absolute; left: 560px; top: 925px; width: 240px; text-align: center;
    color: var(--navy); font-weight: 400;
  }
  .side-brand .brand-name { font-size: 20px; letter-spacing: 0.5px; }
  .side-brand .brand-tag { font-size: 10px; letter-spacing: 2px; margin-top: 6px; }
  .footer-info { position: absolute; left: 0; top: 1140px; width: 849px; height: 60px; color: var(--white); }
  .address { position: absolute; left: 48px; top: 12px; display: flex; align-items: center; gap: 10px; font-size: 15px; line-height: 1.2; }
  .phone { position: absolute; left: 244px; top: 20px; display: flex; align-items: center; gap: 8px; font-size: 17px; font-weight: 600; letter-spacing: 0.5px; }
  .socials { position: absolute; left: 560px; top: 24px; display: flex; gap: 0; }
  .socials span { width: 95px; text-align: center; font-size: 14px; font-weight: 600; }
</style>
</head>
<body>
<main class="flyer">
  <svg class="backdrop" width="849" height="1200" viewBox="0 0 849 1200" aria-hidden="true">
    <defs>
      <linearGradient id="sunset" x1="1" y1="0" x2="0.2" y2="1">
        <stop offset="0" stop-color="#e85a17"/>
        <stop offset="0.55" stop-color="#f29c34"/>
        <stop offset="1" stop-color="#f9ca4a"/>
      </linearGradient>
      <linearGradient id="sea" x1="0" y1="0" x2="0.3" y2="1">
        <stop offset="0" stop-color="#080a28"/>
        <stop offset="0.5" stop-color="#23274a"/>
        <stop offset="1" stop-color="#0a0d2c"/>
      </linearGradient>
      <linearGradient id="footerBand" x1="0" y1="0" x2="1" y2="0">
        <stop offset="0" stop-color="#e85a17"/>
        <stop offset="0.5" stop-color="#f6a23a"/>
        <stop offset="1" stop-color="#e85a17"/>
      </linearGradient>
    </defs>
    <!-- corner accents -->
    <path class="corner-orange" d="M0 25 L74 98 Q98 122 74 146 L0 215 Z" fill="var(--orange)"/>
    <path class="corner-navy" d="M0 190 Q6 176 18 188 L64 236 Q72 245 64 254 L18 300 Q6 312 0 300 Z" fill="var(--navy)"/>
    <!-- faint wheel decoration area -->
    <path role="img" aria-label="Faint ship's wheel decoration" d="M0 560 Q20 560 18 640 A195 195 0 0 1 0 1065 Z" fill="var(--mist)" opacity="0.7"/>
    <!-- hero shapes -->
    <path class="hero-accent" d="M849 510 L849 625 L745 730 C700 775 640 797 560 797 C490 797 440 775 400 745 L700 600 Z" fill="url(#sunset)"/>
    <path role="img" aria-label="Dark stormy sea photograph" class="hero-photo" d="M420 0 L849 0 L849 520 L700 670 C640 730 560 750 480 748 C290 745 143 590 143 420 C143 320 180 250 240 190 Z" fill="url(#sea)"/>
    <!-- footer band -->
    <path d="M0 1105 Q424 1118 849 1105 L849 1200 L0 1200 Z" fill="url(#footerBand)"/>
    <path d="M0 1140 Q424 1096 849 1140 L849 1200 L0 1200 Z" fill="var(--navy)"/>
  </svg>

  <div class="hero-brand">
    <div class="brand-name">KELPWICK HARBOR</div>
    <div class="brand-tag">MARINE SERVICES</div>
  </div>

  <h2 class="intro">
    <span class="lead">Our Company</span><br>
    <span class="strong">Specializes In</span>
  </h2>

  <ul class="services">
    <li><span class="bullet"></span>Boat Engine Diagnostic/Repair</li>
    <li><span class="bullet"></span>Engine Service</li>
    <li><span class="bullet"></span>Electronic Installation And Repairs</li>
    <li><span class="bullet"></span>Bottom Paint</li>
    <li><span class="bullet"></span>Detailing</li>
    <li><span class="bullet"></span>Winterization And Shrink Wrapping</li>
  </ul>

  <div class="side-brand">
    <div class="brand-name">KELPWICK HARBOR</div>
    <div class="brand-tag">MARINE SERVICES</div>
  </div>

  <footer class="footer-info">
    <div class="address">
      <svg width="22" height="28" viewBox="0 0 22 28" aria-hidden="true">
        <path d="M11 0 A11 11 0 0 1 22 11 C22 18 11 28 11 28 C11 28 0 18 0 11 A11 11 0 0 1 11 0 Z" fill="var(--white)"/>
        <circle cx="11" cy="11" r="4.5" fill="var(--navy)"/>
      </svg>
      <span>Lorem Ipsum, No 7<br>Ny City</span>
    </div>
    <div class="phone">
      <svg width="26" height="26" viewBox="0 0 24 24" aria-hidden="true">
        <path d="M6.6 10.8a15.1 15.1 0 0 0 6.6 6.6l2.2-2.2a1 1 0 0 1 1-.25 11.4 11.4 0 0 0 3.6.57 1 1 0 0 1 1 1V20a1 1 0 0 1-1 1A17 17 0 0 1 3 4a1 1 0 0 1 1-1h3.5a1 1 0 0 1 1 1c0 1.25.2 2.45.57 3.57a1 1 0 0 1-.25 1z" fill="var(--white)"/>
      </svg>
      <span>+ 123 456 789</span>
    </div>
    <div class="socials">
      <span>Snapwave</span>
      <span>Friendbook</span>
      <span>Chirper</span>
    </div>
  </footer>
</main>
</body>
</html>
```